WordPress Theme creation and installation from a PSD Website homepage file

Wordpress theme from PSD file:
I need a Wordpress website installed. I have written content and a PSD file that is very close to being complete for a wordpress theme as it is. It was created for a full website homepage by a designer here and is an unflattened PSD file.
I want to modify it just a bit to have a table of contents panel below the main image so that users can click through the content I have written. The job will entail creating the theme from the PSD, installing it to the BrimHaven hosting account with contact us panel working, and installing the written content from a doc file. The table of contents panel simply needs to mimic the look of the existing PSD file.
This WordPress site is a simplified version of the website I am creating. It will have a contact us submission form, and some links that bring up prewritten content.
On the attached JPG example file, you can see the white area that I want just turned in to the content area and the "Table of Contents Here" text is where the table of contents panel will be, with content to the right and below it.

```html
<!DOCTYPE html>
<html lang="en">
<head>
<meta charset="utf-8">
<title>Ashgrove Attorneys</title>
<link rel="stylesheet" href="https://fonts.googleapis.com/css2?family=Source+Sans+3:wght@400;600&family=Arimo:wght@400;700&family=Noto+Serif:wght@700&display=swap">
<style>
:root{
  --navy:#0d4a86;
  --blue:#1a5d96;
  --blue-light:#1f9fd6;
  --red:#c8201f;
  --orange:#e0662c;
  --ink:#333;
  --footer:#313131;
  --footer-text:#d4d4d4;
  --gold:#f2c94c;
  --link:#5cb3e8;
  --white:#fff;
}
*{box-sizing:border-box;margin:0;padding:0}
html,body{width:890px;height:1200px;overflow:hidden;background:var(--white)}
body{position:relative;font-family:"Arimo",Arial,sans-serif;color:var(--ink);font-size:9.5px;line-height:15px}
.abs{position:absolute}
h2,h3,.nav a{font-family:"Source Sans 3",Helvetica,sans-serif;font-weight:400}

/* header */
.site-header{left:0;top:0;width:890px;height:74px;background:var(--white)}
.brand{left:146px;top:18px;width:324px;font-family:"Source Sans 3",Helvetica,sans-serif;font-weight:600;font-size:30px;line-height:36px;color:var(--navy)}
.callout{left:476px;top:0;width:271px;height:71px;background:linear-gradient(#f4f4f4,#d9d9d9);box-shadow:0 1px 3px rgba(0,0,0,.35);text-align:center}
.callout-label{font-family:"Noto Serif",Georgia,serif;font-weight:700;font-size:14.5px;color:#3a3a3a;margin-top:3px}
.callout-phone{font-family:"Noto Serif",Georgia,serif;font-weight:700;font-size:34px;line-height:40px;color:var(--navy)}
.callout-phone span{color:var(--red);font-size:26px}

/* hero */
.hero{left:0;top:74px;width:890px;height:461px;background:linear-gradient(180deg,#eceded,#dcdde0)}
.hero-photo{left:154px;top:80px;width:380px;height:455px;background:linear-gradient(180deg,#d9cfc6 0,#c9b8aa 45%,#3a3b40 78%,#1d1e22 100%)}
.nav{left:379px;top:86px;width:373px;height:34px;border-radius:4px;background:linear-gradient(#1b7cc7,#0b4f8f);display:flex;align-items:center;padding-left:12px}
.nav a{color:var(--white);text-decoration:none;font-size:10.5px;padding:0 9px;border-right:1px solid rgba(255,255,255,.25);line-height:18px}
.nav a:nth-child(4){border-right:0}
.lang{margin-left:6px;display:flex;align-items:center;gap:6px;background:#0a3f74;border-radius:3px;padding:2px 8px;color:var(--white);font-size:10px;font-family:"Source Sans 3",sans-serif}
.contact-panel{left:533px;top:131px;width:218px;height:394px;background:#b8c0c9;border-radius:5px;padding:6px}
.contact-inner{width:100%;height:100%;border-radius:5px;background:linear-gradient(160deg,#1b6fb8 0,#0c4a86 40%,#093a6b 100%);text-align:center;padding-top:8px}
.contact-title{color:var(--white);font-family:"Source Sans 3",sans-serif;font-weight:600;font-size:25px;line-height:31px;text-shadow:0 1px 2px rgba(0,0,0,.5)}
.contact-title em{font-style:normal;color:var(--gold)}
.field{display:block;margin:6px auto 0;width:158px;height:21px;background:var(--white);border-radius:3px;font-size:6.5px;color:#999;text-align:left;padding:4px 7px;line-height:13px}
.field:first-of-type{margin-top:9px}
.field.area{height:179px}
.submit{display:block;margin:9px auto 0;width:158px;height:20px;border-radius:4px;background:linear-gradient(#fafafa,#bdbdbd);font-family:"Source Sans 3",sans-serif;font-weight:600;font-size:15px;line-height:20px;color:#222}

/* content */
.section-title{font-size:19px;line-height:22px;color:#333}
.section-title.alert{color:var(--red)}
.welcome-img{left:146px;top:586px;width:182px;height:70px;border:3px solid #fff;box-shadow:0 0 0 1px #ddd;background:linear-gradient(90deg,#4b3423,#8a6a48 50%,#e7e0d3)}
.welcome-text{left:146px;top:662px;width:186px;font-size:9px;line-height:14.8px}
.btn{display:block;background:linear-gradient(#2d76b3,#0d4a86);color:var(--white);font-weight:700;font-size:9.5px;line-height:20px;text-align:center;border-radius:3px;width:62px;height:20px}
.practice{left:349px;width:192px;height:50px}
.practice .thumb{position:absolute;left:0;top:0;width:56px;height:50px;border:2px solid #fff;box-shadow:0 0 0 1px #ddd}
.practice h3{position:absolute;left:67px;top:-2px;color:var(--blue);font-size:11px}
.practice p{position:absolute;left:67px;top:12px;width:128px;font-size:9px;line-height:13px}
.rule{left:349px;width:192px;height:1px;background:#ddd}
.faq{left:553px;width:192px;height:56px}
.faq .video{position:absolute;left:0;top:0;width:63px;height:51px;background:linear-gradient(#c9c9c9,#3d3d3d 60%,#222)}
.faq .q{position:absolute;left:70px;top:-4px;width:124px;color:var(--red);font-size:9px;line-height:14.5px}
.faq .a{position:absolute;left:70px;top:25px;width:124px;font-size:9px;line-height:13px}
.faq .more{position:absolute;right:0;top:48px;color:var(--red);font-style:italic;font-size:8px;line-height:10px}

.info-strip{left:146px;top:833px;width:598px;height:99px;border:1px solid #ddd;border-radius:4px;background:linear-gradient(#fff,#f2f2f2);display:flex}
.info{flex:1;padding:8px 18px 0 18px;position:relative;box-shadow:6px 0 8px -6px rgba(0,0,0,.2)}
.info:last-child{box-shadow:none}
.info h3{font-size:15.5px;line-height:18px;color:#333}
.info h3.accent{color:var(--blue-light)}
.info p{margin-top:6px;font-size:8.5px;line-height:11.5px;text-align:justify}
.info .read{position:absolute;right:26px;top:77px;color:var(--orange);font-size:8.5px}

/* footer */
.footer{left:0;top:950px;width:890px;height:250px;background:var(--footer)}
.footer-col{color:var(--footer-text)}
.footer-title{color:var(--white);font-size:15px;line-height:18px}
.arrows{left:356px;top:978px;color:#888;font-size:13px;letter-spacing:8px}
.badge{left:146px;width:48px;height:45px;background:#6e1a14;border:2px solid #e8e8e8}
.member-text{left:206px;width:176px;font-size:8.5px;line-height:14.5px;text-align:justify}
.foot-btn{width:60px;height:19px;line-height:19px;font-size:9px}
.office{left:427px;top:998px;width:165px;font-size:8.5px;line-height:15px}
.office-brand{font-family:"Source Sans 3",Helvetica,sans-serif;font-weight:600;font-size:15px;line-height:18px;color:#bdbdbd;margin-bottom:4px}
.office dl{display:grid;grid-template-columns:84px 1fr}
.office a{color:var(--link);text-decoration:none}
.office strong{display:block;color:var(--white);font-size:10px;margin-top:9px}
.office .hours{margin-top:3px;color:var(--white)}
.social{left:612px;width:140px;height:26px;display:flex;align-items:center;gap:15px;font-size:9.5px}
.social i{display:block;width:25px;height:25px;border-radius:4px;background:#5a7fa8}
.copyright{left:540px;top:1168px;width:204px;text-align:right;font-size:8px;line-height:12px;color:#aaa}
</style>
</head>
<body>

<header class="site-header abs">
  <div class="brand abs">Ashgrove Attorneys</div>
  <div class="callout abs">
    <div class="callout-label">CALL for a FREE CONSULTATION</div>
    <div class="callout-phone"><span>(800)</span> 555-0142</div>
  </div>
</header>

<section class="hero abs"></section>
<div class="hero-photo abs" role="img" aria-label="Portrait photograph of a smiling attorney in a dark blazer and white shirt"></div>

<nav class="nav abs">
  <a href="#">Our Story</a><a href="#">Your Stories</a><a href="#">Our Services</a><a href="#">Your Case</a>
  <span class="lang">
    <svg width="18" height="11" viewBox="0 0 18 11"><rect width="18" height="11" fill="#fff"/><rect width="18" height="2" fill="#c8201f"/><rect y="4" width="18" height="1.5" fill="#c8201f"/><rect y="7.5" width="18" height="1.5" fill="#c8201f"/><rect width="8" height="5.5" fill="#1b3f7a"/></svg>
    English
    <svg width="7" height="5" viewBox="0 0 7 5"><path d="M0 0h7L3.5 5z" fill="#fff"/></svg>
  </span>
</nav>

<aside class="contact-panel abs">
  <div class="contact-inner">
    <div class="contact-title">Contact Us Now<br>For <em>FREE</em></div>
    <div class="field">Name</div>
    <div class="field">Phone Number</div>
    <div class="field">Email for Reply</div>
    <div class="field area">Tell us about your case</div>
    <div class="submit">Click for Contact</div>
  </div>
</aside>

<h2 class="section-title abs" style="left:146px;top:554px">Welcome to our site</h2>
<div class="welcome-img abs" role="img" aria-label="Photograph of a gavel, scales of justice and an open law book"></div>
<p class="welcome-text abs">Lorem ipsum dolor sit amet, consectetur adipiscing elit. Fusce accumsan, elit a suscipit sagittis, tortor sapien cursus risus, non rhoncus lectus nunc ac nulla.<br>Aliquam molestie, mi et imperdiet euismod, dui purus auctor tellus, et interdum lacus lectus et ante. Sed accumsan sollicitudin sapien, sit amet adipiscing turpis gravida ac.</p>
<a class="btn abs" style="left:146px;top:790px">Learn More</a>

<h2 class="section-title abs" style="left:349px;top:554px">Practice Areas</h2>
<div class="practice abs" style="top:588px">
  <div class="thumb" role="img" aria-label="Photograph of a person injured after a fall" style="background:linear-gradient(135deg,#f1f1f1,#cfc6bf)"></div>
  <h3>Slip and Fall Injury</h3><p>Lorem ipsum dolor sit amet, consectetur adipiscing elit.</p>
</div>
<div class="rule abs" style="top:644px"></div>
<div class="practice abs" style="top:655px">
  <div class="thumb" role="img" aria-label="Photograph of a damaged red car after an accident" style="background:linear-gradient(135deg,#8f8f8f,#c52a2a 55%,#6b6b6b)"></div>
  <h3>Auto Accident</h3><p>Lorem ipsum dolor sit amet, consectetur adipiscing elit.</p>
</div>
<div class="rule abs" style="top:711px"></div>
<div class="practice abs" style="top:721px">
  <div class="thumb" role="img" aria-label="Photograph of a dog bite on a hand" style="background:linear-gradient(135deg,#2f4a2a,#8a6a4c 60%,#3a3022)"></div>
  <h3>Dog Bite Injury</h3><p>Lorem ipsum dolor sit amet, consectetur adipiscing elit.</p>
</div>
<a class="btn abs" style="left:349px;top:790px">Learn More</a>

<h2 class="section-title alert abs" style="left:553px;top:554px">Top 10 questions</h2>
<div class="faq abs" style="top:586px">
  <div class="video" role="img" aria-label="Video still of three attorneys answering a question"></div>
  <p class="q">Sed ut perspiciatis unde omnis iste natus error?</p>
  <p class="a">Lorem ipsum dolor sit amet, consectetur adipiscing elit.</p>
  <span class="more">more...</span>
</div>
<div class="faq abs" style="top:652px">
  <div class="video" role="img" aria-label="Video still of three attorneys answering a question"></div>
  <p class="q">Sed ut perspiciatis unde omnis iste natus error?</p>
  <p class="a">Lorem ipsum dolor sit amet, consectetur adipiscing elit.</p>
  <span class="more">more...</span>
</div>
<div class="faq abs" style="top:719px">
  <div class="video" role="img" aria-label="Video still of three attorneys answering a question"></div>
  <p class="q">Sed ut perspiciatis unde omnis iste natus error?</p>
  <p class="a">Lorem ipsum dolor sit amet, consectetur adipiscing elit.</p>
  <span class="more">more...</span>
</div>

<section class="info-strip abs">
  <div class="info"><h3 class="accent">Our Purpose</h3><p>Lorem Ipsum is simply dummy text of the printing and typesetting industry. Lorem Ipsum has been the industry's standard dummy text</p><span class="read">Read More &gt;&gt;</span></div>
  <div class="info"><h3>What an Attorney Does</h3><p>Lorem Ipsum is simply dummy text of the printing and typesetting industry. Lorem Ipsum has been the industry's standard dummy text</p><span class="read">Read More &gt;&gt;</span></div>
  <div class="info"><h3>Why Choose Us</h3><p>Lorem Ipsum is simply dummy text of the printing and typesetting industry. Lorem Ipsum has been the industry's standard dummy text</p><span class="read">Read More &gt;&gt;</span></div>
</section>

<footer class="footer abs"></footer>
<h2 class="footer-title abs" style="left:146px;top:976px">Membership &amp; Accreditation</h2>
<span class="arrows abs">&lsaquo;&rsaquo;</span>
<div class="badge abs" style="top:1005px"></div>
<p class="member-text footer-col abs" style="top:1001px">Lorem ipsum dolor sit amet, consectetur adipiscing elit. Fusce accumsan, elit a suscipit sagittis, tortor sapien cursus risus, non rhoncus lectus nunc ac nulla.</p>
<a class="btn foot-btn abs" style="left:327px;top:1052px">Learn More</a>
<div class="badge abs" style="top:1084px"></div>
<p class="member-text footer-col abs" style="top:1080px">Lorem ipsum dolor sit amet, consectetur adipiscing elit. Fusce accumsan, elit a suscipit sagittis, tortor sapien cursus risus, non rhoncus lectus nunc ac nulla.</p>
<a class="btn foot-btn abs" style="left:327px;top:1131px">Learn More</a>

<h2 class="footer-title abs" style="left:427px;top:969px">Main Office</h2>
<div class="office footer-col abs">
  <div class="office-brand">Ashgrove Attorneys</div>
  <p>4120 Larch Lane<br>Glasgow, G12 7QT.</p>
  <dl style="margin-top:3px"><dt>Toll - Free:</dt><dd>+1 800 xxx xxxx</dd><dt>Telephone:</dt><dd>+1 800 xxx xxxx</dd></dl>
  <p>Email : <a href="#">hello@ashgrovelaw.com</a></p>
  <strong>Office Hours:</strong>
  <p class="hours">8:30 a.m. to 5:30 p.m.<br>(Pacific), M-F</p>
</div>

<h2 class="footer-title abs" style="left:612px;top:969px">Connect with Us</h2>
<div class="social footer-col abs" style="top:997px"><i></i>Chirpline</div>
<div class="social footer-col abs" style="top:1025px"><i></i>Friendwall</div>
<div class="social footer-col abs" style="top:1054px"><i></i>Circleo +</div>
<div class="social footer-col abs" style="top:1083px"><i></i>ClipStream</div>

<p class="copyright abs">Copyright &copy; 2012, Ashgrove.<br>All Rights Reserved. | Legal &nbsp;| &nbsp;Privacy Policy</p>

</body>
</html>
```